Wordpress Design Project for Skip Hire company

Redgum Skip Hire is a Skip Hire company based in the Western Suburbs of Melbourne (Australia) and was established in 1995.
The colours of the Redgum Skip Hire logo are Pantone 188C (Burgundy) and 424C (Grey). We would like the site to include these colours throughout the site.

The current Redgum Skip Hire site (www.redgumskiphire.example.au) has been in operation for a number of years and as we have recently commenced a project to update the Logo and Corporate ID, a new Website is also appropriate.

The Redgum Skip Hire site only needs to be a simple site and is unlikely to consist of more than 20 pages. The site is primarily used for people to find our contact details, delivery areas and the measurements/size of of the bins we hire to our customers.

Industry/Entity Type

It Company

Requirements
Must have
• A contact page template (which sends an email) which can be used for a main contact page as well as long form response pages to enhance our 'call to action'
A separate enquiry/order form with configurable options will also be required.
A category (products) page will be required which will list all of our bins, a configurable excerpt of the page contents along with a single photo of each bin (a slider may be used also).
We also require the ability for potential customers to look each bin on it's own page as well as a large image, information about each bin and our terms and conditions.
We would also like configurable titles and meta code for each page.
The site will also need the ability to integrate with Trackwell Stats.

```html
<!DOCTYPE html>
<html lang="en">
<head>
<meta charset="utf-8">
<title>Redgum Skip Hire – Walk in Bins</title>
<link href="https://fonts.googleapis.com/css2?family=Alfa+Slab+One&family=Oswald:wght@500&family=PT+Sans:ital,wght@0,400;0,700;1,700&family=Arimo:ital,wght@0,400;0,700;1,700&display=swap" rel="stylesheet">
<style>
:root{
  --burgundy:#a61c34;
  --burgundy-dark:#7e1626;
  --red:#d8322b;
  --orange:#f07d18;
  --grey:#58595b;
  --grey-mid:#8a8a8a;
  --grey-light:#e6e6e6;
  --footer:#454545;
  --text:#333;
  --white:#fff;
}
*{box-sizing:border-box;margin:0;padding:0}
html,body{width:1078px;height:1200px;overflow:hidden}
body{background:linear-gradient(90deg,var(--burgundy-dark),var(--burgundy) 20%,var(--burgundy) 80%,var(--burgundy-dark));font-family:"Arimo",Arial,sans-serif;color:var(--text)}
.stage{position:relative;width:1150px;height:1280px;transform:scale(.9375);transform-origin:0 0}
.page{position:absolute;left:75px;top:0;width:1000px;height:1280px;background:var(--white)}
.abs{position:absolute}

/* header */
.header{left:0;top:0;width:1000px;height:105px;background:linear-gradient(#fff,#f3f3f3)}
.brand{left:30px;top:14px;font-family:"PT Sans",sans-serif;font-weight:700;font-size:36px;color:var(--burgundy);line-height:40px;width:200px}
.brand span{display:block;white-space:nowrap}
.search{left:768px;top:14px;width:208px;height:28px;border:1px solid #ddd;border-radius:14px;background:linear-gradient(#fff,#eee);font-size:12px;color:#999;padding:6px 16px}
.search svg{position:absolute;right:10px;top:7px}
.nav{left:416px;top:58px;display:flex;font-family:"Oswald",sans-serif;font-size:18px;letter-spacing:.5px;color:var(--grey-mid)}
.nav a{display:block;height:30px;line-height:30px;text-decoration:none;color:inherit}
.nav .current{width:113px;text-align:center;border-radius:15px;background:linear-gradient(#8a8a8a,#6f6f6f);color:var(--white);margin-right:21px}
.nav .item{margin-right:60px}
.nav .item:last-child{margin-right:0}

/* hero */
.hero{left:0;top:105px;width:1000px;height:393px;background:linear-gradient(180deg,#b9d3d8 0%,#a9c877 22%,#7fb22f 45%,#5f9a22 70%,#4c8018 100%)}
.hero .bin{position:absolute;left:475px;top:140px;width:460px;height:250px;background:linear-gradient(#f5c61a,#d9a60d);border-radius:4px;opacity:.95}
.hero-title{left:40px;top:148px;color:var(--white);font-family:"Alfa Slab One",serif;white-space:nowrap}
.hero-title .small{font-size:33px;line-height:40px;letter-spacing:1px}
.hero-title .big{font-size:54px;line-height:58px;letter-spacing:3px;color:#a8162a;-webkit-text-stroke:2px #fff}
.hero-title .big span{color:var(--orange)}
.hero-title .sub{font-size:24px;line-height:32px;margin-left:6px;letter-spacing:.5px}
.hero-rule{left:42px;top:276px;width:425px;border-top:2px dotted rgba(255,255,255,.8)}
.hero-text{left:44px;top:294px;width:420px;color:var(--white);font-size:12px;line-height:18px}
.hero-text em{font-weight:700}
.btn-call{left:313px;top:390px;width:152px;height:43px;border:2px solid #fff;border-radius:10px;background:linear-gradient(#dc3a5f,#b4173d);color:#fff;font-family:"PT Sans",sans-serif;font-weight:700;font-size:17px;padding:8px 11px;box-shadow:0 2px 4px rgba(0,0,0,.3);white-space:nowrap}
.btn-call span{color:#f57d8f;margin-left:4px}
.dots{left:10px;top:477px;display:flex;gap:4px}
.dots span{width:47px;height:47px;border-radius:50%;background:#e8e8e8;border:2px solid #fff;box-shadow:0 1px 3px rgba(0,0,0,.2);font:700 13px/43px "PT Sans",serif;text-align:center;color:#444}
.dots .on{background:var(--orange);color:#fff}

/* content */
h2{font-family:"PT Sans",sans-serif;font-weight:700;font-size:24px;color:var(--grey);white-space:nowrap}
h2 em{font-style:normal;color:var(--red)}
.rule{border-top:1px dotted #bbb}
.photo{left:18px;top:600px;width:186px;height:144px;border:3px solid #fff;box-shadow:0 0 3px rgba(0,0,0,.3);background:linear-gradient(#9cc0e2 0%,#c7d6e0 45%,#8a8f8c 70%,#6d6a63 100%)}
.copy{font-size:12px;line-height:18px;color:var(--text)}
.copy em{font-weight:700}
.card{width:324px;height:216px;border:1px solid #e5e5e5;border-radius:12px;background:linear-gradient(#fff,#f2f2f2);overflow:hidden}
.card .corner{position:absolute;left:0;top:0}
.card h3{position:absolute;left:50px;top:28px;font-family:"PT Sans",sans-serif;font-size:19px;font-weight:700;color:var(--grey);white-space:nowrap}
.card h3 em{font-style:normal;color:#c3173b}
.card .line{position:absolute;left:52px;top:58px;width:260px;border-top:1px dotted #aaa}
.card ul{position:absolute;left:28px;top:76px;list-style:none;font-size:12px;color:var(--text)}
.card li{padding-left:16px;position:relative;line-height:20px}
.card li::before{content:"";position:absolute;left:0;top:6px;border-left:5px solid #c3173b;border-top:4px solid transparent;border-bottom:4px solid transparent}
.card.no ul li{line-height:24px}
.card.no ul li::before{top:8px}

/* form */
.field{left:713px;width:249px;height:36px;border:1px solid #d6d6d6;border-radius:18px;background:linear-gradient(#f3f3f3,#fff);font-size:12px;color:#444;padding:10px 17px;box-shadow:inset 0 2px 3px rgba(0,0,0,.08)}
.field.area{left:717px;width:245px;height:132px;border-radius:14px;padding:16px 14px}
.btn-submit{left:851px;top:1003px;width:112px;height:37px;border:2px solid #fff;border-radius:18px;background:linear-gradient(#dc3a5f,#b4173d);box-shadow:0 0 3px rgba(0,0,0,.4);color:#fff;font-size:13px;text-align:center;line-height:33px}

/* footer */
.footer{left:0;top:1110px;width:1000px;height:170px;background:var(--footer);color:#eee;font-size:12px}
.f-brand{left:15px;top:12px;font-family:"PT Sans",sans-serif;font-weight:700;font-size:32px;line-height:36px;color:#b5b5b5;width:200px}
.f-brand span{display:block;white-space:nowrap}
.f-accept{left:13px;top:97px}
.pay{top:120px;width:58px;height:36px;border:2px solid #fff;background:#6e6e6e;font-size:11px;text-align:center;line-height:32px;color:#fff}
.divider{top:12px;height:150px;border-left:1px dotted #999}
.f-links{left:308px;top:20px;width:418px;text-align:center}
.f-links span{margin:0 8px}
.f-follow{left:308px;top:56px;width:418px;text-align:center}
.social{top:80px;width:38px;height:38px;border-radius:50%;background:#5b6f8a;border:2px solid #ddd}
.f-copy{left:308px;top:145px;width:418px;text-align:center}
.f-contact{right:12px;top:12px;text-align:right}
.f-contact h4{font-family:"PT Sans",sans-serif;font-weight:400;font-size:20px;color:#bbb}
.f-contact strong{display:block;font-family:"PT Sans",sans-serif;font-size:19px;margin-top:6px;color:#fff}
.f-contact p{line-height:18px;margin-top:2px}
.phone{right:12px;top:122px;display:flex;align-items:center;gap:10px;font-family:"Oswald",sans-serif;font-size:28px;color:#c9c9c9;letter-spacing:1px}
</style>
</head>
<body>
<div class="stage">
<div class="page">

  <header class="header abs">
    <div class="brand abs"><span>Redgum</span><span>Skip Hire</span></div>
    <div class="search abs">Searching ...
      <svg width="10" height="10" viewBox="0 0 10 10"><circle cx="4" cy="4" r="3" fill="none" stroke="#333" stroke-width="1.6"/><line x1="6.2" y1="6.2" x2="9" y2="9" stroke="#333" stroke-width="1.8"/></svg>
    </div>
    <nav class="nav abs">
      <a class="current" href="#">Home</a>
      <a class="item" href="#">Product List</a>
      <a class="item" href="#">Delivery Area</a>
      <a class="item" href="#">Contact Us</a>
    </nav>
  </header>

  <section class="hero abs" role="img" aria-label="Rolling green countryside with a large yellow walk-in bin on the grass">
    <div class="bin"></div>
  </section>
  <div class="hero-title abs">
    <div class="small">Suppliers of</div>
    <div class="big">Walk in <span>Bins</span></div>
    <div class="sub">for domestic &amp; commercial use.</div>
  </div>
  <div class="hero-rule abs"></div>
  <p class="hero-text abs"><em>Redgum Skip Hire supplies walk in bins for domestic and commercial use.</em><br>Our bins range in size from 4 cubic metres through to 10 cubic metres. We also have 20 cubic metre bins. All bins have gates for easy access and most will fit in a standard driveway....</p>
  <div class="btn-call abs">Call Us Now <span>&raquo;&raquo;</span></div>
  <div class="dots abs"><span>01.</span><span class="on">02.</span><span>03.</span><span>04.</span></div>

  <h2 class="abs" style="left:21px;top:547px"><em>Company</em> Overview</h2>
  <div class="rule abs" style="left:21px;top:584px;width:611px"></div>
  <div class="photo abs" role="img" aria-label="Bin delivery truck parked on a gravel yard"></div>
  <p class="copy abs" style="left:213px;top:603px;width:430px"><em>Redgum Skip Hire supplies walk in bins for domestic and commercial use.</em><br>Our bins range in size from 4 cubic metres through to 10 cubic metres. We also have 20 cubic metre bins. All bins have gates for easy access and most will fit in a standard driveway.<br>We deliver in the western suburbs of Melbourne and over the Westgate Bridge to South Melbourne. Bin hire is for a maximum period of up to 3 days. The day of delivery is day 1, the day of pick up is day 3.</p>

  <h2 class="abs" style="left:21px;top:776px;font-size:19px"><em>Council</em> Permits</h2>
  <p class="copy abs" style="left:21px;top:808px;width:650px">A Council permit is required for bins placed outside your property i.e. on the road, nature strip or in a laneway/ROW. We will apply to Council for a permit on your behalf. Please call us for current permit rates for your area.</p>

  <div class="card abs" style="left:11px;top:877px">
    <svg class="corner" width="74" height="76"><polygon points="0,0 74,0 0,76" fill="#c3173b"/></svg>
    <h3><em>What can you</em> put in the bin?</h3>
    <div class="line"></div>
    <ul>
      <li>Household goods</li>
      <li>Furniture and furnishings</li>
      <li>Garden clippings (surcharge applies)</li>
      <li>Builders waste</li>
      <li>Rock, soil or concrete in 4mt &amp; 6 mt only</li>
      <li>Tyres and mattresses (at extra cost)</li>
    </ul>
  </div>
  <div class="card no abs" style="left:347px;top:877px">
    <svg class="corner" width="74" height="76"><polygon points="0,0 74,0 0,76" fill="#ee5a1e"/></svg>
    <h3 style="left:47px"><em style="color:#ea5a1b">What can’t you</em> put in the bin?</h3>
    <div class="line"></div>
    <ul>
      <li>No asbestos</li>
      <li>No hazardous or toxic waste</li>
      <li>No flammable waste</li>
      <li>No batteries</li>
      <li>No liquid waste</li>
    </ul>
  </div>

  <h2 class="abs" style="left:712px;top:547px"><em>Call to</em> Action</h2>
  <div class="rule abs" style="left:712px;top:584px;width:260px"></div>
  <p class="copy abs" style="left:714px;top:596px;width:262px">In hac habitasse platea dictumst. Donec commodo, purus sit amet luctus placerat, nunc nulla congue enim, vitae vulputate mauris ligula nec orci.</p>
  <div class="field abs" style="top:698px">Your Name</div>
  <div class="field abs" style="top:749px">Your Email</div>
  <div class="field abs" style="top:800px">Your Phone</div>
  <div class="field area abs" style="top:855px">Additional Information</div>
  <div class="btn-submit abs">Submit Form</div>

  <footer class="footer abs">
    <div class="f-brand abs"><span>Redgum</span><span>Skip Hire</span></div>
    <p class="f-accept abs">We accept Cash, Cheque, CardOne &amp; PayLink</p>
    <div class="pay abs" style="left:28px">CardOne</div>
    <div class="pay abs" style="left:102px">PayLink</div>
    <div class="divider abs" style="left:308px"></div>
    <p class="f-links abs">Home <span>~</span> Product List <span>~</span> Delivery Area <span>~</span> Contact Us</p>
    <p class="f-follow abs">Follow Us On:</p>
    <div class="social abs" style="left:430px" aria-label="Friendly"></div>
    <div class="social abs" style="left:478px;background:#4a8fb8" aria-label="Chirper"></div>
    <div class="social abs" style="left:526px;background:#3f7ba6" aria-label="Linkwork"></div>
    <div class="social abs" style="left:574px;background:#555" aria-label="Plusone"></div>
    <p class="f-copy abs">Redgum Skip Hire, Copyright © 2012-13, Privacy Policy</p>
    <div class="divider abs" style="left:729px"></div>
    <div class="f-contact abs">
      <h4>Contact Info</h4>
      <strong>Redgum Skip Hire</strong>
      <p>12 Tallowood Street,<br>Kestrel Bay Vic 3099</p>
    </div>
    <div class="phone abs">
      <svg width="34" height="34" viewBox="0 0 34 34"><circle cx="17" cy="17" r="15.5" fill="none" stroke="#ccc" stroke-width="2"/><path d="M12 9c1.5-1 2.5 0 3 1.5l1 2.5c.3 1-.3 1.6-1 2.1 .8 2 2 3.4 3.6 4.5.6-.7 1.3-1.2 2.2-.8l2.5 1.2c1.4.6 2 1.6.8 3-2 2-5 1.5-8-1.2-3.2-3-5-6.4-5-9.2 0-1.4.4-2.6.9-3.6z" fill="#ccc"/></svg>
      03 9000 4821
    </div>
  </footer>

</div>
</div>
</body>
</html>
```